Landing Page & Email Signature

I am looking for a new landing page as well as an email signature to align with the change in business. I have included the new logo/emblem which I'd like incorporated into the design and the current landing page is www.dornelquip.com.au should you wish to see the old version.

```html
<!DOCTYPE html>
<html lang="en">
<head>
<meta charset="utf-8">
<title>Dornel Quip – Enquire</title>
<link href="https://fonts.googleapis.com/css2?family=Bebas+Neue&family=Roboto:wght@400;500&display=swap" rel="stylesheet">
<style>
  :root {
    --brand-red: #be1e2d;
    --ink: #2b2b2b;
    --muted: #9a9a9a;
    --rule: #cfcfcf;
    --card-left: rgba(255,255,255,0.86);
    --card-right: #ffffff;
    --port-sky: #e6e9ea;
    --port-mid: #b9c2c6;
    --port-deep: #7f8a8f;
  }
  * { box-sizing: border-box; margin: 0; padding: 0; }
  html, body { width: 1200px; height: 675px; overflow: hidden; }
  body { font-family: "Roboto", Arial, sans-serif; color: var(--ink); position: relative; }

  .backdrop {
    position: absolute; inset: 0;
    background:
      radial-gradient(ellipse at 30% 95%, rgba(190,110,70,0.45), transparent 45%),
      radial-gradient(ellipse at 75% 90%, rgba(120,130,100,0.5), transparent 50%),
      linear-gradient(180deg, var(--port-sky) 0%, var(--port-mid) 55%, var(--port-deep) 100%);
  }

  .card { position: absolute; border-radius: 26px; }
  .card--intro { left: 45px; top: 70px; width: 556px; height: 534px; background: var(--card-left); border-radius: 26px 0 0 26px; }
  .card--form { left: 601px; top: 46px; width: 555px; height: 585px; background: var(--card-right); box-shadow: 0 6px 24px rgba(0,0,0,0.12); }

  .abs { position: absolute; }

  .brand { left: 178px; top: 112px; display: flex; align-items: center; gap: 10px; }
  .brand__mark { width: 36px; height: 36px; border-radius: 50%; background: var(--brand-red); }
  .brand__name { font-family: "Bebas Neue", Impact, sans-serif; font-size: 44px; line-height: 1; color: var(--brand-red); }
  .brand__url { left: 214px; top: 174px; font-size: 11px; color: var(--brand-red); font-weight: 500; }

  .headline { font-family: "Bebas Neue", Impact, sans-serif; color: var(--brand-red); line-height: 1; }
  .headline--kicker { left: 177px; top: 222px; font-size: 49px; }
  .headline--main { left: 176px; top: 268px; font-size: 69px; }

  .copy { font-size: 12.5px; line-height: 22px; color: var(--ink); }
  .copy--lead { left: 178px; top: 341px; }
  .copy--proof { left: 178px; top: 400px; }

  .contact { left: 179px; display: flex; align-items: center; gap: 10px; font-size: 12.5px; }
  .contact--phone { top: 460px; font-weight: 500; }
  .contact--mail { top: 490px; }
  .contact__icon { width: 20px; height: 20px; background: var(--brand-red); display: flex; align-items: center; justify-content: center; }

  .legal { left: 178px; top: 565px; font-size: 10px; color: #444; }

  .social { left: 966px; top: 68px; display: flex; gap: 11px; }
  .social__dot { width: 22px; height: 22px; border-radius: 50%; background: var(--brand-red); }

  .headline--form { left: 647px; top: 113px; font-size: 48px; }
  .copy--form { left: 649px; top: 161px; }

  .field { left: 647px; width: 373px; border-bottom: 1px solid var(--rule); }
  .field__label { font-size: 12px; color: var(--muted); letter-spacing: 0.2px; }
  .field__value { font-size: 12.5px; color: var(--ink); margin-top: 7px; padding-bottom: 7px; }
  .field--name { top: 226px; }
  .field--phone { top: 296px; }
  .field--email { top: 366px; }
  .field--message { top: 436px; height: 73px; }

  .cta { left: 900px; top: 532px; width: 122px; height: 35px; background: var(--brand-red); color: #fff; font-size: 12.5px; font-weight: 500; display: flex; align-items: center; justify-content: center; }
</style>
</head>
<body>
  <div class="backdrop" role="img" aria-label="Aerial photograph of a shipping port with stacked containers under a hazy sky"></div>

  <section class="card card--intro"></section>
  <section class="card card--form"></section>

  <div class="abs brand"><span class="brand__mark"></span><span class="brand__name">Dornel Quip</span></div>
  <div class="abs brand__url">www.dornelquip.com.au</div>

  <h2 class="abs headline headline--kicker">We Can Guarantee</h2>
  <h1 class="abs headline headline--main">Your Satisfaction</h1>

  <p class="abs copy copy--lead">Are you ready? We are ready to get it done!<br>Get best service from us to satisfy your current and future needs!</p>
  <p class="abs copy copy--proof">To prove, you may call our clients, who we have been serving for<br>years to hear first-hand testimonies.</p>

  <div class="abs contact contact--phone">
    <span class="contact__icon"><svg width="12" height="12" viewBox="0 0 24 24"><path fill="#fff" d="M6.6 10.8a15.1 15.1 0 0 0 6.6 6.6l2.2-2.2c.3-.3.7-.4 1-.2 1.1.4 2.3.6 3.6.6.6 0 1 .4 1 1V20c0 .6-.4 1-1 1A17 17 0 0 1 3 4c0-.6.4-1 1-1h3.5c.6 0 1 .4 1 1 0 1.3.2 2.5.6 3.6.1.3 0 .7-.2 1z"/></svg></span>
    +61400218736
  </div>
  <div class="abs contact contact--mail">
    <span class="contact__icon"><svg width="12" height="12" viewBox="0 0 24 24"><path fill="#fff" d="M2 5h20v14H2z"/><path fill="none" stroke="#be1e2d" stroke-width="2" d="M2 6l10 7 10-7"/></svg></span>
    hello@dornelquip.com.au
  </div>

  <p class="abs legal">© Copyright 2022 Dornel Quip Transport &amp; Logistics | All Rights Reserved.</p>

  <div class="abs social"><span class="social__dot"></span><span class="social__dot"></span></div>

  <h2 class="abs headline headline--form">We Look Forward</h2>
  <p class="abs copy copy--form">Are you ready? We are ready to get it done!<br>Get best service from us to satisfy your current and future needs!</p>

  <div class="abs field field--name"><div class="field__label">FULL NAME</div><div class="field__value">Your Full Name</div></div>
  <div class="abs field field--phone"><div class="field__label">PHONE NUMBER</div><div class="field__value">Your Phone Number</div></div>
  <div class="abs field field--email"><div class="field__label">EMAIL ADDRESS</div><div class="field__value">Your Email Address</div></div>
  <div class="abs field field--message"><div class="field__label">MESSAGE</div><div class="field__value">Your Detailed Message</div></div>

  <div class="abs cta">ENQUIRE NOW!</div>
</body>
</html>
```